Meadow Lark Honey and Combs produces and sells local raw honey.

The logo is in the files. Use the one with the brown letters. We are looking to have a web page that tells our customers about our products and where they can be purchased. We may take orders and sell from this web page in the future. We would like to have a way for customers to ask questions or provide feedback. I've provided pictures but it will be up to the designer's discretion to use whatever pictures are relevant to the design.

Target Market(s)

Customers in the greater Seattle area.

Coding

Coded - Design and coding required

Number of Pages Required

3 page

Font styles to use
Sans Serif

Colors

Designer to choose colors to be used in the design.

Requirements
Must have
• A message that we produce and sell only pure raw local honey. Raw honey means it has never been flavored, heated, pasteurized, filtered or has additives of any kind. The web page should also let people know where they can find our honey for purchase.

```html
<!DOCTYPE html>
<html lang="en">
<head>
<meta charset="utf-8">
<title>Meadow Lark Honey and Combs</title>
<link href="https://fonts.googleapis.com/css2?family=Lora:wght@400;700&display=swap" rel="stylesheet">
<style>
:root{
  --yellow:#f3f31a;
  --ink:#1a1a1a;
  --brown:#5a3d17;
  --grey-text:#777;
  --white:#ffffff;
}
*{box-sizing:border-box;margin:0;padding:0}
html,body{width:1200px;height:3586px;overflow:hidden}
body{position:relative;background:var(--white);font-family:"Lora",Georgia,serif;color:var(--ink)}
.abs{position:absolute}
a{color:inherit;text-decoration:none}
.btn{position:absolute;background:var(--yellow);border-radius:26px;font-weight:700;font-size:15px;display:flex;align-items:center;justify-content:center;color:var(--ink)}
.ornament{position:absolute;left:565px;width:70px;height:26px;border-radius:13px;background:linear-gradient(90deg,rgba(30,30,30,0) 0%,rgba(30,30,30,.6) 30%,rgba(230,220,30,.85) 50%,rgba(30,30,30,.6) 70%,rgba(30,30,30,0) 100%)}
.section-title{position:absolute;left:0;width:1200px;text-align:center;font-size:42px;line-height:50px;font-weight:400;letter-spacing:1px}

/* hero */
.hero{left:0;top:0;width:1200px;height:580px;background:linear-gradient(180deg,#4d7fc2 0%,#8ea8c6 22%,#4f6a4a 40%,#6b4f7a 62%,#8a5e8e 78%,#3d5a2c 100%)}
.nav-bar{left:0;top:44px;width:1200px;height:62px;background:var(--yellow)}
.nav-link{position:absolute;top:64px;font-size:16px;line-height:20px}
.brand{position:absolute;top:52px;left:470px;width:260px;height:46px;background:var(--white);border-radius:23px;display:flex;align-items:center;justify-content:center;font-size:14px;color:var(--brown);gap:8px}
.brand-dot{width:9px;height:9px;border-radius:50%;background:var(--brown)}
.hero-title{left:0;top:276px;width:1200px;text-align:center;color:var(--white);font-size:58px;line-height:62px;font-weight:400}

/* varietals */
.variety-img{position:absolute;width:131px;height:131px}
.variety-name{position:absolute;font-size:17px;line-height:20px;font-weight:400}
.variety-text{position:absolute;width:140px;font-size:11px;line-height:16px;color:var(--grey-text)}
.view-details{position:absolute;background:var(--yellow);border-radius:10px;font-size:10px;font-weight:700;width:94px;height:20px;display:flex;align-items:center;justify-content:center}

/* about */
.about{left:0;top:1420px;width:1200px;height:444px;background:linear-gradient(135deg,#cfcfcf 0%,#e8e8e8 40%,#bdbdbd 70%,#d9d9d9 100%)}
.about-text{left:300px;width:600px;text-align:center;font-size:11px;line-height:15px}

/* gallery */
.gallery-tile{position:absolute;width:172px;height:171px}

/* calendar */
.season{position:absolute;top:2696px;width:442px;height:258px}
.season-title{position:absolute;width:442px;text-align:center;font-size:30px;line-height:36px;top:54px;font-weight:400}
.season-ornament{position:absolute;left:196px;width:50px;height:22px;border-radius:11px;background:rgba(40,40,40,.5)}

/* swarm band */
.swarm{left:0;top:3028px;width:1200px;height:390px;background:linear-gradient(180deg,#3a3a3a 0%,#252525 55%,#383838 100%)}
.swarm-text{left:0;width:1200px;text-align:center;color:var(--white)}

/* footer */
.footer-link{position:absolute;top:3480px;font-size:15px;line-height:18px}
.footer-brand{position:absolute;top:3472px;left:500px;width:200px;text-align:center;font-size:13px;color:var(--brown);line-height:17px}
.copyright{left:0;top:3538px;width:1200px;text-align:center;font-size:15px}
</style>
</head>
<body>

<header>
  <div class="abs hero" role="img" aria-label="Mountain meadow of pink fireweed in bloom beneath forested hills and blue sky"></div>
  <div class="abs nav-bar"></div>
  <nav>
    <a class="nav-link" style="left:172px">Home</a>
    <a class="nav-link" style="left:255px">About Us</a>
    <a class="nav-link" style="left:360px">Products</a>
    <a class="nav-link" style="left:788px">Locations</a>
    <a class="nav-link" style="left:898px">Faq's</a>
    <a class="nav-link" style="left:975px">Contact Us</a>
  </nav>
  <div class="brand"><span class="brand-dot"></span>Meadow Lark Honey and Combs</div>
  <h1 class="abs hero-title">We Sell Only<br>Pure Raw Local Honey</h1>
  <a class="btn" style="left:480px;top:420px;width:240px;height:54px">Learn More</a>
</header>

<section class="varietals">
  <div class="ornament" style="top:628px" role="img" aria-label="Bee ornament"></div>
  <h2 class="section-title" style="top:668px">HONEY VARIETALS</h2>
  <div class="ornament" style="top:720px;height:22px" role="img" aria-label="Scroll ornament"></div>

  <div class="variety-img" style="left:143px;top:800px;background:linear-gradient(135deg,#1d1d1d,#3b3f45)" role="img" aria-label="Blueberries"></div>
  <div class="view-details" style="left:161px;top:855px">View Details</div>
  <h3 class="variety-name" style="left:292px;top:797px">Blueberry</h3>
  <p class="variety-text" style="left:292px;top:830px">Taken from the tiny white flowers of the blueberry bush, the nectar makes a honey that is fruity and luscious. Many people believe that Blueberry honey is honey to which Blueberry flavor is added; this is not so. It is rich in pollen, so think it will not fall off of a PB and Honey sandwich and has been known to help people with allergies.</p>

  <div class="variety-img" style="left:456px;top:800px;background:linear-gradient(135deg,#c2477f,#6e2a55 60%,#6f8a4a)" role="img" aria-label="Pink fireweed flowers"></div>
  <h3 class="variety-name" style="left:605px;top:797px">Fireweed</h3>
  <p class="variety-text" style="left:605px;top:830px">Taken from the tiny white flowers of the blueberry bush, the nectar makes a honey that is fruity and luscious. Many people believe that Blueberry honey is honey to which Blueberry flavor is added; this is not so. It is rich in pollen, so think it will not fall off of a PB and Honey sandwich and has been known to help people with allergies.</p>

  <div class="variety-img" style="left:767px;top:800px;background:linear-gradient(135deg,#5c7a3c,#e8e6dc 50%,#6f8a4a)" role="img" aria-label="White blackberry blossoms"></div>
  <h3 class="variety-name" style="left:914px;top:797px">Blackberry</h3>
  <p class="variety-text" style="left:914px;top:830px">Taken from the tiny white flowers of the blueberry bush, the nectar makes a honey that is fruity and luscious. Many people believe that Blueberry honey is honey to which Blueberry flavor is added; this is not so. It is rich in pollen, so think it will not fall off of a PB and Honey sandwich and has been known to help people with allergies.</p>

  <div class="variety-img" style="left:143px;top:1088px;background:linear-gradient(135deg,#2f3a1c,#b3b63a 55%,#3d4a22)" role="img" aria-label="Big leaf maple blossoms"></div>
  <h3 class="variety-name" style="left:292px;top:1085px">Big Leaf Maple</h3>
  <p class="variety-text" style="left:292px;top:1118px">Taken from the tiny white flowers of the blueberry bush, the nectar makes a honey that is fruity and luscious. Many people believe that Blueberry honey is honey to which Blueberry flavor is added; this is not so. It is rich in pollen, so think it will not fall off of a PB and Honey sandwich and has been known to help people with allergies.</p>

  <div class="variety-img" style="left:456px;top:1088px;background:linear-gradient(135deg,#3c5a2a,#8fae6a 50%,#2e4420)" role="img" aria-label="Knotweed leaves"></div>
  <h3 class="variety-name" style="left:605px;top:1085px">Knotweed</h3>
  <p class="variety-text" style="left:605px;top:1118px">Taken from the tiny white flowers of the blueberry bush, the nectar makes a honey that is fruity and luscious. Many people believe that Blueberry honey is honey to which Blueberry flavor is added; this is not so. It is rich in pollen, so think it will not fall off of a PB and Honey sandwich and has been known to help people with allergies.</p>

  <div class="variety-img" style="left:767px;top:1088px;background:linear-gradient(135deg,#c74a6a,#d9b13a 45%,#6a3b8a 75%,#4c7a34)" role="img" aria-label="Field of mixed wildflowers"></div>
  <h3 class="variety-name" style="left:914px;top:1085px">Wildflower</h3>
  <p class="variety-text" style="left:914px;top:1118px">Taken from the tiny white flowers of the blueberry bush, the nectar makes a honey that is fruity and luscious. Many people believe that Blueberry honey is honey to which Blueberry flavor is added; this is not so. It is rich in pollen, so think it will not fall off of a PB and Honey sandwich and has been known to help people with allergies.</p>
</section>

<section>
  <div class="abs about" role="img" aria-label="Faded photo of a farmers market honey stall"></div>
  <div class="ornament" style="top:1470px" role="img" aria-label="Bee ornament"></div>
  <h2 class="section-title" style="top:1506px">ABOUT US</h2>
  <div class="ornament" style="top:1558px;height:22px" role="img" aria-label="Scroll ornament"></div>
  <p class="abs about-text" style="top:1610px">Our bees forage across the valleys and hills near the city, gathering nectar from wild blooms, orchards and quiet roadside meadows. Every jar is extracted by hand and bottled raw, never heated, filtered or flavored, so it keeps the taste of the season.</p>
  <p class="abs about-text" style="top:1670px">We are a small family apiary that moves hives through the year to follow the bloom. Come meet us at the market and taste the difference.</p>
  <a class="btn" style="left:480px;top:1750px;width:240px;height:54px">Learn More</a>
</section>

<section>
  <h2 class="section-title" style="top:1970px">PHOTO GALLERY</h2>
  <div class="ornament" style="top:2024px;height:24px" role="img" aria-label="Bee ornament"></div>
  <div class="gallery-tile" style="left:131px;top:2080px;background:linear-gradient(135deg,#111,#2a2a2a)" role="img" aria-label="Dark title card for a market day"></div>
  <div class="gallery-tile" style="left:323px;top:2080px;background:linear-gradient(135deg,#d8d8d8,#3a4a6a 50%,#cfcfcf)" role="img" aria-label="Patterned painted hive boxes"></div>
  <div class="gallery-tile" style="left:516px;top:2080px;background:linear-gradient(135deg,#cfcfcf,#8a4a1e 50%,#d9d9d9)" role="img" aria-label="Jar of honey on a table"></div>
  <div class="gallery-tile" style="left:707px;top:2080px;background:linear-gradient(135deg,#9aa3a6,#2f4a6a 50%,#c8c8c8)" role="img" aria-label="Row of beehives"></div>
  <div class="gallery-tile" style="left:899px;top:2080px;background:linear-gradient(135deg,#7a4d14,#d09a3a 50%,#5a3510)" role="img" aria-label="Honey bees on comb"></div>
  <div class="gallery-tile" style="left:131px;top:2276px;background:linear-gradient(135deg,#3a4a3a,#c8b89a 50%,#3a3a6a)" role="img" aria-label="Beekeeper tending stacked hives"></div>
  <div class="gallery-tile" style="left:323px;top:2276px;background:linear-gradient(135deg,#e6e6e6,#5a6a4a 50%,#2a3a5a)" role="img" aria-label="Beekeeper in suit inspecting hive"></div>
  <div class="gallery-tile" style="left:516px;top:2276px;background:linear-gradient(135deg,#3e5a2a,#d48a1e 50%,#9a5a14)" role="img" aria-label="Jars of honey in the sun"></div>
  <div class="gallery-tile" style="left:707px;top:2276px;background:linear-gradient(135deg,#cfc6b8,#6a3a1a 50%,#e0d8cc)" role="img" aria-label="Honey jars being labelled"></div>
  <div class="gallery-tile" style="left:899px;top:2276px;background:linear-gradient(135deg,#4a5a2a,#8a7a3a 50%,#3a4a22)" role="img" aria-label="Swarm of bees on a branch"></div>
</section>

<section>
  <div class="ornament" style="top:2530px" role="img" aria-label="Bee ornament"></div>
  <h2 class="section-title" style="top:2566px">CALENDAR OF FARMERS MARKETS</h2>
  <div class="ornament" style="top:2620px;height:24px" role="img" aria-label="Scroll ornament"></div>

  <div class="season" style="left:143px;background:linear-gradient(135deg,#f3f31a,#e6e61c 60%,#f3f31a)" role="img" aria-label="Market stall photo under a yellow tint">
    <div class="season-ornament" style="top:26px"></div>
    <h3 class="season-title">Winter</h3>
    <p class="abs" style="left:0;top:130px;width:442px;text-align:center;font-size:22px;line-height:27px">Sundays @ Harbor Square<br>(Elm Street) in Lakemont 11-3.</p>
  </div>

  <div class="season" style="left:610px;background:linear-gradient(135deg,#c9c9c9,#b2b2b2 50%,#d4d4d4)" role="img" aria-label="Faded market stall photo">
    <div class="season-ornament" style="top:26px"></div>
    <h3 class="season-title">Summer</h3>
    <p class="abs" style="left:0;top:120px;width:442px;text-align:center;font-size:12px;line-height:15px">Markets will begin in May and run through September.</p>
    <p class="abs" style="left:30px;top:158px;width:170px;font-size:12px;line-height:15px">Wednesdays 3-7 Cedar Point Park near the boat ramp.</p>
    <p class="abs" style="left:232px;top:158px;width:200px;font-size:12px;line-height:15px">Saturdays 9-3 Millbrook at Alder Park north of Greenleaf.</p>
    <div class="abs" style="left:138px;top:210px;width:166px;height:22px;border-radius:11px;background:var(--yellow);font-size:12px;display:flex;align-items:center;justify-content:center">Sundays to be announced</div>
  </div>
</section>

<section>
  <div class="abs swarm" role="img" aria-label="Dark photo of hives at the edge of a forest"></div>
  <p class="abs swarm-text" style="top:3124px;font-size:27px;line-height:36px">We offer free honey bee swarm removal service within<br>30 miles of Millbrook.</p>
  <p class="abs swarm-text" style="top:3196px;font-size:40px;line-height:48px">Sam Holloway 206 555-0148</p>
  <a class="btn" style="left:480px;top:3284px;width:240px;height:54px">Contact Us</a>
</section>

<footer>
  <a class="footer-link" style="left:222px">Home</a>
  <a class="footer-link" style="left:305px">About Us</a>
  <a class="footer-link" style="left:412px">Products</a>
  <div class="footer-brand">Meadow Lark Honey<br>and Combs</div>
  <a class="footer-link" style="left:720px">Locations</a>
  <a class="footer-link" style="left:830px">Faq's</a>
  <a class="footer-link" style="left:907px">Contact Us</a>
  <p class="abs copyright">© 2018 Company Name &nbsp;|&nbsp; All Rights Reserved</p>
</footer>

</body>
</html>
```